Brinmore Sports Pub. Where the locals go!!

We are creating a sports pub. We are needing a fun website that offers our menu along with an event page and general info. We have some attached links that we really like:
https://www.dolvetts.example/
https://www.cafemiralto.example/
https://www.quillstonepx.example/
We are doing a pirate theme but that is because the area we are in. We would like to see a pirate like in our logo doing something like drinking real time similar to the dolvetts website above.
Target Market(s)
Sports Fans
Industry/Entity Type
Pub, Bar, Restaurant
Coding
Coded - Design and coding required
Number of Pages Required
3 page
Font styles to use
Other font styles liked:
- see uploads
Look and feel

```html
<!DOCTYPE html>
<html lang="en">
<head>
<meta charset="utf-8">
<title>Brinmore Sports Pub</title>
<link rel="stylesheet" href="https://fonts.googleapis.com/css2?family=Rye&family=Alegreya+Sans+SC:wght@700&display=swap">
<style>
:root{
  --bg:#212325;
  --cream:#e8dcc4;
  --red:#c8203a;
  --rule:#9c978d;
  --shade:#3a3a38;
}
*{margin:0;padding:0;box-sizing:border-box}
html,body{width:956px;height:1200px;overflow:hidden;background:var(--bg)}
body{position:relative;color:var(--cream);font-family:"Alegreya Sans SC",sans-serif;font-weight:700;letter-spacing:.04em}
a{color:inherit;text-decoration:none}
.abs{position:absolute}
.nav{display:flex;gap:23px;font-family:"Rye",serif;font-size:11.5px;letter-spacing:.02em}
.site-nav{left:88px;top:48px}
.rule{height:2px;background:var(--rule)}
.social{display:flex;gap:14px}
.social span{width:16px;height:16px;border-radius:50%;background:var(--cream);display:block}
.brand-seal{left:394px;top:21px;width:170px;height:170px;border-radius:50%;background:var(--cream);display:flex;align-items:center;justify-content:center;text-align:center;color:var(--bg);font-family:"Rye",serif;font-size:17px;line-height:1.25;box-shadow:0 0 0 3px var(--bg),0 0 0 5px var(--cream)}
.heading{font-family:"Rye",serif;color:var(--red);letter-spacing:.05em}
.heading.lg{font-size:22px}
.heading.sm{font-size:11.5px}
.body-copy{font-size:12.5px;line-height:18px}
.art{background:radial-gradient(circle,#cfc3a8 0%,#8a816f 55%,var(--bg) 100%);opacity:.85}
.contact-row{display:flex;align-items:center;gap:9px;font-size:13px}
.icon{width:20px;height:20px;border-radius:50%;background:var(--cream);display:flex;align-items:center;justify-content:center}
.specials p{font-size:12.5px;margin-bottom:10.6px}
.menu-link{font-size:13.5px}
</style>
</head>
<body>
<header>
  <nav class="abs nav site-nav"><a href="#">Home</a><a href="#">Menu</a><a href="#">Events</a><a href="#">Contact</a></nav>
  <div class="abs rule" style="left:86px;top:112px;width:286px"></div>
  <div class="abs rule" style="left:584px;top:112px;width:286px"></div>
  <div class="abs brand-seal">BRINMORE<br>SPORTS PUB</div>
  <div class="abs social" style="left:752px;top:47px" aria-label="Social links"><span></span><span></span><span></span><span></span></div>
</header>

<section class="about">
  <h2 class="abs heading lg" style="left:88px;top:293px">About Us</h2>
  <div class="abs body-copy" style="left:88px;top:327px;width:310px">Lorem ipsum dolor sit amet consectetur adipiscing elit sed do eiusmod tempor incididunt ut labore et dolore magna aliqua.</div>
  <div class="abs body-copy" style="left:88px;top:405px;width:310px">Adipiscing elit sed do eiusmod tempor incididunt ut labore et dolore magna aliqua quis ipsum suspendisse ultrices gravida.</div>
  <div class="abs contact-row" style="left:87px;top:490px">
    <span class="icon"><svg width="12" height="9" viewBox="0 0 12 9"><rect x=".6" y=".6" width="10.8" height="7.8" rx="1" fill="none" stroke="#212325" stroke-width="1.2"/><path d="M1 1l5 4 5-4" fill="none" stroke="#212325" stroke-width="1.2"/></svg></span>info@brinmorepub.example</div>
  <div class="abs contact-row" style="left:87px;top:520px">
    <span class="icon"><svg width="11" height="11" viewBox="0 0 24 24"><path d="M6.6 10.8a15 15 0 006.6 6.6l2.2-2.2a1 1 0 011-.25 11 11 0 003.6.6 1 1 0 011 1V20a1 1 0 01-1 1A17 17 0 013 4a1 1 0 011-1h3.5a1 1 0 011 1c0 1.25.2 2.45.57 3.57a1 1 0 01-.25 1z" fill="#212325"/></svg></span>+405 555 0190</div>

  <h3 class="abs heading sm" style="left:497px;top:300px">Location</h3>
  <div class="abs body-copy" style="left:497px;top:319px;line-height:22px">48 Harbor Lane<br>Dunmore 18044</div>
  <h3 class="abs heading sm" style="left:497px;top:387px">Bar Hours</h3>
  <div class="abs body-copy" style="left:497px;top:406px;line-height:22px">Monday- 5pm - 12am<br>Tuesday- Closed<br>Wednesday &amp; Thursday- 5pm - 12am<br>Friday &amp; Saturday- 5pm - 1am<br>Sunday- 2pm - 12am</div>
  <div class="abs art" role="img" aria-label="Illustration of a skeleton in a barrel raising a mug" style="left:668px;top:208px;width:148px;height:194px;border-radius:40%"></div>
</section>

<div class="abs rule" style="left:86px;top:661px;width:359px"></div>
<div class="abs rule" style="left:511px;top:661px;width:359px"></div>
<div class="abs art" role="img" aria-label="Small compass rose ornament" style="left:458px;top:642px;width:40px;height:40px;border-radius:50%"></div>

<section class="specials">
  <div class="abs art" role="img" aria-label="Illustration of a foaming beer mug" style="left:210px;top:765px;width:130px;height:148px;border-radius:30%"></div>
  <h2 class="abs heading lg" style="left:415px;top:755px">Specials</h2>
  <div class="abs" style="left:415px;top:793px">
    <p>Tuesday (4 - 9) — $5 Old Fashioned</p>
    <p>Wednesday (4 - 9) — Half Off Wine</p>
    <p>Thursday (3 - 7) — $12 Pizza and Boilermaker</p>
    <p>Friday (3 - 6) — Half Price Well Drinks</p>
    <p>Saturday (11 - 4) — Half Price Mimosas</p>
  </div>
  <a class="abs heading menu-link" href="#" style="left:415px;top:963px">View Full Menu</a>
</section>

<footer>
  <div class="abs art" role="img" aria-label="Compass illustration peeking over the footer line" style="left:405px;top:1033px;width:125px;height:59px;border-radius:60px 60px 0 0"></div>
  <div class="abs rule" style="left:84px;top:1091px;width:789px;height:1.5px"></div>
  <div class="abs brand-seal" style="left:95px;top:1115px;width:66px;height:66px;font-size:8px;box-shadow:0 0 0 2px var(--bg),0 0 0 3px var(--cream)">BRINMORE<br>SPORTS PUB</div>
  <nav class="abs nav" style="left:345px;top:1141px;gap:29px;font-size:12.5px"><a href="#">Home</a><a href="#">Menu</a><a href="#">Events</a><a href="#">Contact</a></nav>
  <div class="abs social" style="left:757px;top:1139px;gap:11px" aria-label="Social links"><span style="width:20px;height:20px"></span><span style="width:20px;height:20px"></span><span style="width:20px;height:20px"></span><span style="width:20px;height:20px"></span></div>
</footer>
</body>
</html>
```